Ridgeback Petroleum Ventures, LLC

Our website (www.ridgebackpetroventures.example) is poorly done and dated. I want to redo it with one main page and wide format photos or oil & gas drilling and production. Perhaps all of the pages listed on the left side of the existing site could be viewed by scrolling down further on the new main page. I want something clean and easy to navigate.

Target Market(s)

Other oil and gas companies and people that we have contacted regarding selling or leasing their mineral rights. These people will come to our website to research our company and become more comfortable doing business with us.

Industry/Entity Type

Oil And Gas

Coding

Coded - Design and coding required

Number of Pages Required

1 page

Font styles to use
Serif

Requirements
Must have
• Clean and uncluttered. Nice, clear wide format picture or oil well or rig and landscape.

```html
<!DOCTYPE html>
<html lang="en">
<head>
<meta charset="utf-8">
<title>Ridgeback Petroleum Ventures, LLC</title>
<link href="https://fonts.googleapis.com/css2?family=Cabin:wght@400;500;600;700&family=Lato:ital,wght@0,400;0,700;1,400&display=swap" rel="stylesheet">
<style>
:root{
  --orange:#f07a22;
  --dark:#231f1f;
  --nav:#1f1d1d;
  --ink:#222;
  --text:#444;
  --footer:#2a2626;
  --footer-bar:#1c1919;
  --line:#cfcfcf;
}
*{margin:0;padding:0;box-sizing:border-box}
html,body{width:1200px;height:2209px;overflow:hidden}
body{position:relative;background:#fff;font-family:'Lato',sans-serif;color:var(--text)}
.abs{position:absolute}
.top-rule{left:0;top:0;width:1200px;height:3px;background:var(--orange)}
.brand{left:98px;top:28px;display:flex;align-items:center;gap:10px}
.brand-dot{width:34px;height:34px;border-radius:50%;background:var(--orange)}
.brand-name{font-family:'Cabin',sans-serif;font-weight:700;font-size:27px;color:var(--ink);line-height:1.05;width:330px}
.contact-item{top:38px;display:flex;align-items:center;gap:12px}
.contact-icon{width:42px;height:42px;flex:none;border-radius:50%;background:var(--orange);border:3px solid #ffd2a8;display:flex;align-items:center;justify-content:center}
.contact-label{font-size:13px;color:#555}
.contact-value{font-size:14px;font-weight:700;color:var(--ink);margin-top:3px;white-space:nowrap}
.nav{left:0;top:111px;width:1200px;height:42px;background:var(--nav)}
.nav ul{list-style:none;display:flex;position:absolute;left:100px;top:0;height:42px}
.nav li{font-family:'Cabin',sans-serif;font-weight:600;font-size:13px;color:#fff;height:42px;line-height:44px;text-align:center;border-right:1px solid #3a3636}
.nav li.active{background:var(--orange)}
.hero{left:0;top:153px;width:1200px;height:473px;background:linear-gradient(180deg,#4f7fae 0%,#7fa6c9 30%,#2f5f94 65%,#1d4277 100%)}
.hero-rig{left:0;top:153px;width:720px;height:473px;background:linear-gradient(135deg,rgba(60,62,66,.75),rgba(110,100,70,.55) 60%,rgba(40,60,90,0))}
.welcome{left:790px;top:339px;width:311px;height:100px;background:rgba(28,44,68,.85);color:#fff;font-family:'Cabin',sans-serif;font-weight:600;font-size:21px;line-height:31px;text-align:right;padding:12px 20px}
.cta{left:910px;top:427px;width:172px;height:40px;background:var(--orange);border:1px solid #ffc79a;color:#fff;font-family:'Cabin',sans-serif;font-weight:600;font-size:16px;text-align:center;line-height:38px}
.history{left:0;top:626px;width:1200px;height:302px;background:linear-gradient(180deg,#fff,#f1f1f1)}
.section-title{width:1200px;left:0;text-align:center;font-family:'Cabin',sans-serif;font-weight:700;font-size:30px;color:var(--ink);letter-spacing:.5px}
.section-title span{color:var(--orange)}
.section-title.on-dark{color:#fff}
.divider{left:410px;width:380px;height:14px}
.history-text{left:130px;top:746px;width:940px;text-align:center;font-size:13.5px;line-height:27.5px;color:#333}
.about{left:0;top:928px;width:1200px;height:465px;background:linear-gradient(180deg,#1a2433 0%,#3a4a60 45%,#1b2230 100%)}
.card{width:489px;height:124px;background:rgba(120,130,150,.55);padding:22px 28px;color:#fff}
.card h3{font-family:'Cabin',sans-serif;font-weight:600;font-size:22px;margin-bottom:8px}
.card p{font-size:13px;line-height:20px;color:#eee}
.card .plus{position:absolute;right:6px;bottom:6px;width:14px;height:14px;background:#fff;color:#333;font-size:13px;line-height:13px;text-align:center;font-weight:700}
.avatar{width:110px;height:110px;border-radius:50%;border:4px solid var(--ink);background:linear-gradient(160deg,#c9c1b8,#8c8c8c)}
.avatar.active{border-color:var(--orange)}
.t-name{width:200px;text-align:center;font-family:'Cabin',sans-serif;font-weight:600;font-size:14.5px;color:var(--ink)}
.t-name.active{color:var(--orange)}
.quote-box{left:97px;top:1709px;width:1004px;height:141px;border:1px solid #ddd;border-radius:2px;padding:26px 30px;text-align:center;font-style:italic;font-size:13.5px;line-height:27px;color:#333}
.qmark{font-family:Georgia,serif;font-size:46px;color:#f7c9a4;font-style:normal;line-height:0;vertical-align:-16px}
.footer{left:0;top:1902px;width:1200px;height:257px;background:var(--footer)}
.footer-bar{left:0;top:2159px;width:1200px;height:50px;background:var(--footer-bar);color:#ddd;font-size:14.5px;text-align:center;line-height:50px;font-family:'Cabin',sans-serif}
.f-title{font-family:'Cabin',sans-serif;font-weight:700;font-size:16px;color:#fff;letter-spacing:.5px}
.f-rule{height:1px;background:#444}
.f-links{font-size:12.5px;color:#fff;line-height:32.5px;list-style:none}
.f-links li::before{content:"›";margin-right:8px}
.f-addr{font-size:12.5px;color:#eee;line-height:19px;padding-left:25px}
.f-field{background:#3a3636;border:1px solid #5a5555;color:#ddd;font-size:11px;padding:4px 10px}
.send{left:1026px;top:2065px;width:74px;height:49px;background:var(--orange);color:#fff;font-family:'Cabin',sans-serif;font-weight:700;font-size:12px;text-align:center;line-height:49px}
.vsep{width:1px;background:#3c3838}
</style>
</head>
<body>
<div class="abs top-rule"></div>

<header>
  <div class="abs brand"><div class="brand-dot"></div><div class="brand-name">Ridgeback Petroleum<br>Ventures, LLC</div></div>
  <div class="abs contact-item" style="left:625px">
    <div class="contact-icon"><svg width="18" height="18" viewBox="0 0 24 24"><path fill="#222" d="M6.6 10.8a15 15 0 0 0 6.6 6.6l2.2-2.2a1 1 0 0 1 1-.25 11 11 0 0 0 3.6.6 1 1 0 0 1 1 1V20a1 1 0 0 1-1 1A17 17 0 0 1 3 4a1 1 0 0 1 1-1h3.5a1 1 0 0 1 1 1 11 11 0 0 0 .6 3.6 1 1 0 0 1-.25 1z"/></svg></div>
    <div><div class="contact-label">Call Us:</div><div class="contact-value">405.555.0172</div></div>
  </div>
  <div class="abs contact-item" style="left:795px">
    <div class="contact-icon"><svg width="18" height="18" viewBox="0 0 24 24"><path fill="#222" d="M6.6 10.8a15 15 0 0 0 6.6 6.6l2.2-2.2a1 1 0 0 1 1-.25 11 11 0 0 0 3.6.6 1 1 0 0 1 1 1V20a1 1 0 0 1-1 1A17 17 0 0 1 3 4a1 1 0 0 1 1-1h3.5a1 1 0 0 1 1 1 11 11 0 0 0 .6 3.6 1 1 0 0 1-.25 1z"/></svg></div>
    <div><div class="contact-label">Email Us:</div><div class="contact-value" style="font-size:12.5px">inquiry@ridgebackpetroventures.example</div></div>
  </div>
  <nav class="abs nav"><ul>
    <li class="active" style="width:113px">HOME</li>
    <li style="width:124px">HISTORY</li>
    <li style="width:133px">ABOUT US</li>
    <li style="width:219px">AVAILABLE PROSPECTS</li>
    <li style="width:107px">TEXAS</li>
    <li style="width:149px">OKLAHOMA</li>
    <li style="width:153px">CONTACT US</li>
  </ul></nav>
</header>

<section>
  <div class="abs hero" role="img" aria-label="Offshore oil and gas production platform at dusk above a rough blue sea"></div>
  <div class="abs hero-rig"></div>
  <div class="abs welcome">Welcome to Ridgeback<br>Petroleum Ventures, LLC</div>
  <div class="abs cta">Contact Us Today</div>
</section>

<section>
  <div class="abs history"></div>
  <h2 class="abs section-title" style="top:668px">OUR <span>HISTORY</span></h2>
  <svg class="abs divider" style="top:716px" viewBox="0 0 380 14"><line x1="0" y1="7" x2="175" y2="7" stroke="#ccc"/><line x1="205" y1="7" x2="380" y2="7" stroke="#ccc"/><circle cx="190" cy="8" r="5" fill="#ccc"/></svg>
  <p class="abs history-text">Ridgeback Petroleum Ventures, LLC was founded in 2009 by Warren Marlowe. In 2010 Grant Marlowe &amp; Harold Marlowe joined the company. In 2011, Owen Fenwick joined the company as a Petroleum Engineer and in 2014, became a partner. Ridgeback has expanded their business, and currently has offices located in Fort Worth and Oklahoma City. Since 2010 Ridgeback has acquired more than 18,000 net acres of leasehold in Texas, Oklahoma and Kansas. During the same time, the company has also purchased in excess of 7,500 mineral acres primarily in Oklahoma and to a lesser extent, East Texas. In addition, Ridgeback has participated in many wells with top tier operators.</p>
</section>

<section>
  <div class="abs about" role="img" aria-label="Darkened offshore rig photo behind the team section"></div>
  <h2 class="abs section-title on-dark" style="top:972px">ABOUT US</h2>
  <svg class="abs divider" style="top:1019px" viewBox="0 0 380 14"><line x1="0" y1="7" x2="175" y2="7" stroke="#6a7588"/><line x1="205" y1="7" x2="380" y2="7" stroke="#6a7588"/><circle cx="190" cy="8" r="5" fill="#8893a5"/></svg>
  <div class="abs card" style="left:98px;top:1063px"><h3>Warren Marlowe</h3><p>Warren has been an independent landman since 2003. Since starting Ridgeback, he has successfully put together and sold multiple lease...</p><div class="plus">+</div></div>
  <div class="abs card" style="left:612px;top:1063px"><h3>Harold Marlowe</h3><p>Harold has over 30 years of experience as a petroleum geologist. He was most recently the East Texas Exploration Manager at Keystone Energy...</p><div class="plus">+</div></div>
  <div class="abs card" style="left:98px;top:1216px"><h3>Grant Marlowe</h3><p>Grant spent six years at Keystone Energy, managing commercial real estate transactions. He left in March of 2010 to join Warren in expanding...</p><div class="plus">+</div></div>
  <div class="abs card" style="left:612px;top:1216px"><h3>Owen Fenwick</h3><p>Previously, Owen spent five years at Prairieline Energy Inc., where he worked as a completion engineer, production engineer and reservoir...</p><div class="plus">+</div></div>
</section>

<section>
  <h2 class="abs section-title" style="top:1436px">CLIENT <span>TESTIMONIAL</span></h2>
  <svg class="abs divider" style="top:1483px" viewBox="0 0 380 14"><line x1="0" y1="7" x2="175" y2="7" stroke="#ccc"/><line x1="205" y1="7" x2="380" y2="7" stroke="#ccc"/><circle cx="190" cy="8" r="5" fill="#ccc"/></svg>
  <svg class="abs" style="left:180px;top:1570px" width="16" height="30"><polyline points="13,2 3,15 13,28" fill="none" stroke="#cfe0e6" stroke-width="2"/></svg>
  <svg class="abs" style="left:998px;top:1570px" width="16" height="30"><polyline points="3,2 13,15 3,28" fill="none" stroke="#cfe0e6" stroke-width="2"/></svg>
  <div class="abs avatar active" style="left:238px;top:1529px" role="img" aria-label="Client portrait"></div>
  <div class="abs avatar" style="left:444px;top:1529px" role="img" aria-label="Client portrait"></div>
  <div class="abs avatar" style="left:643px;top:1529px" role="img" aria-label="Client portrait"></div>
  <div class="abs avatar" style="left:850px;top:1529px" role="img" aria-label="Client portrait"></div>
  <div class="abs t-name active" style="left:199px;top:1657px">Lorem Ipsum Dolor</div>
  <div class="abs t-name" style="left:399px;top:1657px">Lorem Ipsum Dolor</div>
  <div class="abs t-name" style="left:598px;top:1657px">Lorem Ipsum Dolor</div>
  <div class="abs t-name" style="left:805px;top:1657px">Lorem Ipsum Dolor</div>
  <div class="abs quote-box"><span class="qmark">&ldquo;</span>&nbsp; Lorem Ipsum is simply dummy text of the printing and typesetting industry. Lorem Ipsum has been the industry's standard dummy text ever since the 1500s, when an unknown printer took a galley of type and scrambled it to make a type specimen book. It has survived not only five centuries, but also the leap into electronic typesetting, remaining essentially unchanged. It was pn tof Letraset sheets. &nbsp;<span class="qmark">&rdquo;</span></div>
  <svg class="abs" style="left:268px;top:1690px" width="24" height="20"><polygon points="0,0 24,0 24,20" fill="#fff"/><polyline points="0,0 24,20 24,0" fill="none" stroke="#ddd"/></svg>
</section>

<footer>
  <div class="abs footer"></div>
  <div class="abs vsep" style="left:377px;top:1950px;height:170px"></div>
  <div class="abs vsep" style="left:740px;top:1950px;height:170px"></div>
  <div class="abs f-title" style="left:98px;top:1941px">QUICK LINK</div>
  <div class="abs f-rule" style="left:98px;top:1974px;width:224px"></div>
  <ul class="abs f-links" style="left:98px;top:1982px"><li>Home</li><li>History</li><li>About Us</li><li>Available Prospects</li></ul>
  <ul class="abs f-links" style="left:248px;top:1982px"><li>Texas</li><li>Oklahoma</li><li>Contact Us</li></ul>
  <div class="abs f-title" style="left:427px;top:1941px">CONTACT US</div>
  <div class="abs f-rule" style="left:427px;top:1974px;width:270px"></div>
  <svg class="abs" style="left:425px;top:1994px" width="12" height="16" viewBox="0 0 12 16"><path fill="#fff" d="M6 0a6 6 0 0 0-6 6c0 4.5 6 10 6 10s6-5.5 6-10a6 6 0 0 0-6-6zm0 8.5A2.5 2.5 0 1 1 6 3.5a2.5 2.5 0 0 1 0 5z"/></svg>
  <div class="abs f-addr" style="left:427px;top:1991px;width:290px">Fort Worth Office<br>480 Commerce Street Suite 310 Fort Worth, Texas 76102</div>
  <svg class="abs" style="left:425px;top:2062px" width="12" height="16" viewBox="0 0 12 16"><path fill="#fff" d="M6 0a6 6 0 0 0-6 6c0 4.5 6 10 6 10s6-5.5 6-10a6 6 0 0 0-6-6zm0 8.5A2.5 2.5 0 1 1 6 3.5a2.5 2.5 0 0 1 0 5z"/></svg>
  <div class="abs f-addr" style="left:427px;top:2059px;width:290px">Oklahoma City Office<br>210 Harvey Avenue Suite 4B Oklahoma City, Oklahoma 73102</div>
  <div class="abs f-title" style="left:790px;top:1941px">CONTACT US</div>
  <div class="abs f-rule" style="left:790px;top:1974px;width:310px"></div>
  <div class="abs f-field" style="left:790px;top:1994px;width:310px;height:27px">Name</div>
  <div class="abs f-field" style="left:790px;top:2030px;width:310px;height:26px">Email</div>
  <div class="abs f-field" style="left:790px;top:2065px;width:223px;height:49px">Message</div>
  <div class="abs send">SEND</div>
  <div class="abs footer-bar">© Copyright 2017 by Ridgeback Petroleum Ventures, LLC .</div>
</footer>
</body>
</html>
```